Intermodal Trucking Company Website

My client is a trucking company that takes the containers you see on the back of a ship or railroad car and delivers them in the midwestern part of the United States. Here are some of their competitors Websites and their logo to use as part of the design.

http://www.vardenhollow.example/
https://www.pelrix.example/
http://www.brackwaterfreightlines.example/
https://www.mbv-lo.example/

Industry/Entity Type

Trucking Company

Number of Pages Required

2 page

Requirements
Must have
• Website must be professional and the design needs to be suitable for a responsive Website.
Should not have
• Please do not submit designs with misspellings. Designs with misspellings will be eliminated.

```html
<!DOCTYPE html>
<html lang="en">
<head>
<meta charset="utf-8">
<title>Twin Ridge Freight Inc — Intermodal Trucking</title>
<link rel="stylesheet" href="https://fonts.googleapis.com/css2?family=Oswald:wght@400;500&family=Poppins:wght@400;500;600;700&family=Arvo:wght@700&display=swap">
<style>
:root{
  --cream:#ecebdf;
  --orange:#d65b34;
  --yellow:#f8f33a;
  --ink:#222222;
  --text:#555555;
  --panel:#e9e9e9;
  --line:#cfcfcf;
  --footer:#464646;
  --footer-dark:#2e2e2e;
  --white:#ffffff;
}
*{box-sizing:border-box;margin:0;padding:0}
html,body{width:1200px;height:2432px;overflow:hidden}
body{position:relative;background:var(--white);font-family:'Poppins',sans-serif;color:var(--ink)}
.abs{position:absolute}
.heading{font-family:'Oswald',sans-serif;font-weight:500;text-transform:uppercase;color:var(--ink)}

/* header */
.site-header{left:0;top:0;width:1200px;height:164px;background:var(--cream)}
.header-contact{left:73px;top:74px;font-size:19px;font-weight:500}
.header-contact span{margin:0 8px;color:#999}
.brand{left:0;width:1200px;top:62px;display:flex;justify-content:center;align-items:center;gap:12px;font-family:'Oswald',sans-serif;font-size:30px;font-weight:500;color:var(--orange)}
.brand-dot{width:22px;height:22px;border-radius:50%;background:var(--orange)}
.search{left:936px;top:71px;width:188px;height:34px;background:var(--white);border:1px solid var(--line);font-size:15px;color:#888;padding:6px 10px}
.search svg{position:absolute;right:10px;top:8px}

/* nav */
.main-nav{left:0;top:164px;width:1200px;height:44px;background:var(--orange)}
.main-nav a{position:absolute;top:9px;font-family:'Oswald',sans-serif;font-size:19px;color:var(--white);text-decoration:none;transform:translateX(-50%);white-space:nowrap}
.social{display:flex;gap:6px}
.social i{display:block;width:25px;height:25px;border:2px solid var(--white);border-radius:50%}
.main-nav .social{position:absolute;left:1037px;top:9px}

/* hero */
.hero{left:0;top:208px;width:1200px;height:549px;background:linear-gradient(180deg,#5f86b4 0%,#8fb0d3 40%,#4b6e95 75%,#2f435a 100%)}
.hero-title{left:96px;top:260px;font-family:'Arvo',serif;font-weight:700;font-size:37px;line-height:40px;color:var(--white);text-transform:uppercase}
.hero-sub{left:96px;top:355px;font-size:24px;font-weight:500;color:var(--white)}
.btn-yellow{background:var(--yellow);color:var(--ink);font-weight:600;text-transform:uppercase;display:flex;align-items:center;justify-content:center}
.hero-btn{left:96px;top:415px;width:144px;height:37px;font-size:17px}
.slider-arrow{top:465px;width:52px;height:52px;background:#111;display:flex;align-items:center;justify-content:center}

/* about */
.about-title{left:73px;top:798px;font-size:23px}
.about-text{left:73px;top:842px;width:390px;font-size:14px;line-height:26px;color:var(--text)}
.about-image{left:470px;top:770px;width:304px;height:268px;background:radial-gradient(ellipse at 55% 55%,#3f64b8 0%,#7e93bf 45%,#ffffff 75%)}
.services-panel{left:774px;top:757px;width:426px;height:333px;background:var(--yellow)}
.services-title{left:793px;top:798px;font-size:23px}
.services-list{left:793px;top:842px;list-style:none}
.services-list li{font-size:14px;height:35.2px;display:flex;align-items:center;gap:10px}
.services-list li::before{content:"";border-left:7px solid var(--ink);border-top:5px solid transparent;border-bottom:5px solid transparent}

/* feature band */
.band{left:0;top:1090px;width:1200px;height:326px;background:linear-gradient(180deg,#8d9aa8 0%,#6a5c55 45%,#3b3a3c 100%)}
.feature-card{top:1224px;width:250px;height:109px;background:var(--white);transform:skewX(-8deg)}
.feature-label{top:1268px;width:250px;text-align:center;font-size:18px;font-weight:500;line-height:22px}
.feature-icon{top:1184px;width:80px;height:80px;border-radius:50%;background:var(--yellow);display:flex;align-items:center;justify-content:center}

/* widgets */
.widget{top:1468px;width:332px;height:240px;background:var(--panel);border:1px solid var(--line)}
.widget-title{top:1481px;font-size:22px;padding-bottom:6px;border-bottom:2px solid var(--line);width:296px}
.field{height:39px;background:var(--white);border:1px solid var(--line);font-size:15px;color:#777;padding:9px 12px}
.field.select::after{content:"";position:absolute;right:12px;top:16px;border-top:8px solid #333;border-left:7px solid transparent;border-right:7px solid transparent}
.btn-orange{background:var(--orange);color:var(--white);font-weight:700;font-size:21px;text-transform:uppercase;display:flex;align-items:center;justify-content:center}
.testimonial-title{left:430px;width:340px;top:1473px;text-align:center;font-size:22px}
.testimonial-quote{left:430px;top:1519px;width:340px;text-align:center;font-size:14px;line-height:24px;color:var(--text)}
.quote-mark{font-family:'Arvo',serif;font-size:40px;color:#c9c9c9;line-height:0;vertical-align:-14px}
.testimonial-name{left:430px;top:1648px;width:340px;text-align:center;font-size:15px;font-weight:600;color:#444}
.testimonial-role{left:430px;top:1670px;width:340px;text-align:center;font-size:13px;color:var(--text)}
.dots{left:580px;top:1697px;display:flex;gap:4px}
.dots i{width:10px;height:10px;border-radius:50%;background:#d5d5d5}
.dots i:first-child{background:#555}

/* promos */
.promo{top:1763px;width:512px;height:288px}
.promo-photo{position:absolute;inset:0}
.promo-title{left:36px;top:32px;font-family:'Oswald',sans-serif;font-weight:500;font-size:36px;line-height:34px;color:var(--white);text-transform:uppercase;letter-spacing:-.5px}
.promo-text{left:36px;top:156px;width:420px;font-size:14px;line-height:22px;color:var(--white)}
.promo-btn{left:36px;top:215px;width:102px;height:26px;font-size:12px}

/* footer */
.site-footer{left:0;top:2115px;width:1200px;height:269px;background:var(--footer);color:var(--white)}
.footer-title{top:2145px;font-size:16px;font-weight:600;color:var(--white)}
.quick-links{left:73px;top:2183px;list-style:none}
.quick-links li{font-size:14px;height:32.5px;display:flex;align-items:center;gap:10px;color:#e5e5e5}
.quick-links li::before{content:"";border-left:5px solid #bbb;border-top:4px solid transparent;border-bottom:4px solid transparent}
.map{left:344px;top:2189px;width:241px;height:158px;background:linear-gradient(135deg,#e8e4da,#d9dccf);border:2px solid #777}
.contact-info{left:605px;top:2183px;width:140px;font-size:14px;line-height:25px;color:#f0f0f0;white-space:nowrap}
.footer-social{left:605px;top:2273px}
.footer-social i{border-color:#ddd}
.footer-field{background:var(--white);font-size:14px;color:#777;padding:8px 12px}
.copyright{left:0;top:2384px;width:1200px;height:48px;background:var(--footer-dark);color:#eee;font-size:15px;display:flex;align-items:center;justify-content:center;gap:12px}
</style>
</head>
<body>

<header class="abs site-header">
  <div class="abs header-contact">Kansas City, KS<span>|</span>913-555-0148</div>
  <div class="abs brand"><span class="brand-dot"></span>Twin Ridge Freight Inc</div>
  <div class="abs search">Search
    <svg width="18" height="18" viewBox="0 0 18 18"><circle cx="7.5" cy="7.5" r="5.5" fill="none" stroke="#222" stroke-width="2"/><line x1="11.5" y1="11.5" x2="16.5" y2="16.5" stroke="#222" stroke-width="2"/></svg>
  </div>
</header>

<nav class="abs main-nav">
  <a style="left:337px">HOME</a>
  <a style="left:435px">ABOUT</a>
  <a style="left:576px">NEWS AND EVENTS</a>
  <a style="left:730px">SERVICES</a>
  <a style="left:848px">CONTACT</a>
  <div class="social"><i></i><i></i><i></i></div>
</nav>

<section class="abs hero" role="img" aria-label="Photo of a blue semi truck cab against a cloudy sky"></section>
<h1 class="abs hero-title">Lorem ipsum dolor<br>sit consectetur</h1>
<p class="abs hero-sub">Sed do eiusmod tempor incididunt</p>
<a class="abs btn-yellow hero-btn">Learn more</a>
<div class="abs slider-arrow" style="left:0">
  <svg width="28" height="20" viewBox="0 0 28 20"><path d="M26 10H3M11 2L3 10l8 8" fill="none" stroke="#fff" stroke-width="3"/></svg>
</div>
<div class="abs slider-arrow" style="left:1148px">
  <svg width="28" height="20" viewBox="0 0 28 20"><path d="M2 10h23M17 2l8 8-8 8" fill="none" stroke="#fff" stroke-width="3"/></svg>
</div>

<h2 class="abs heading about-title">About Twin Ridge Freight</h2>
<p class="abs about-text">Lorem ipsum dolor sit amet, consectetur adipiscing elit, sed do eiusmod tempor incididunt ut labore et dolore magna aliqua. Ut enim ad minim veniam, quis nostrud exercitation ullamco laboris nisi ut aliquip ex ea commodo consequat. Duis aute irure dolor in reprehenderit in voluptate velit esse cillum dolore eu fugiat nulla pariatur.</p>
<div class="abs about-image" role="img" aria-label="Photo of a blue semi truck on a white background"></div>
<div class="abs services-panel"></div>
<h2 class="abs heading services-title">Comprehensive Services</h2>
<ul class="abs services-list">
  <li>Drayage, Heavy Haul</li>
  <li>Hazmat, Liquids, ISO Tank</li>
  <li>Warehousing, Cross-Dock, Block &amp; Brace</li>
  <li>Short/Long Term Storage</li>
  <li>Transload, Break Bulk, Consolidation Loads</li>
  <li>Truckload Brokerage</li>
</ul>

<section class="abs band" role="img" aria-label="Photo of a red semi truck hauling a trailer at sunset"></section>
<div class="abs feature-card" style="left:215px"></div>
<div class="abs feature-card" style="left:475px"></div>
<div class="abs feature-card" style="left:736px"></div>
<div class="abs feature-icon" style="left:300px">
  <svg width="40" height="32" viewBox="0 0 40 32"><rect x="2" y="4" width="36" height="24" fill="none" stroke="#222" stroke-width="3"/><path d="M9 8v16M15 8v16M21 8v16M27 8v16M33 8v16" stroke="#222" stroke-width="2"/></svg>
</div>
<div class="abs feature-icon" style="left:560px">
  <svg width="44" height="32" viewBox="0 0 44 32"><rect x="2" y="4" width="26" height="18" fill="#222"/><path d="M28 10h8l6 7v5H28z" fill="#222"/><circle cx="10" cy="26" r="4" fill="#222"/><circle cx="34" cy="26" r="4" fill="#222"/></svg>
</div>
<div class="abs feature-icon" style="left:821px">
  <svg width="40" height="40" viewBox="0 0 40 40"><circle cx="15" cy="15" r="8" fill="none" stroke="#222" stroke-width="5" stroke-dasharray="4 2.3"/><circle cx="15" cy="15" r="3" fill="#222"/><circle cx="29" cy="28" r="6" fill="none" stroke="#222" stroke-width="4" stroke-dasharray="3 2"/></svg>
</div>
<p class="abs feature-label" style="left:215px">Trucking Shipping<br>Services</p>
<p class="abs feature-label" style="left:475px">Specialty Freight &amp;<br>Shipping Services</p>
<p class="abs feature-label" style="left:736px">Logistics<br>Management</p>

<!-- tracking -->
<div class="abs widget" style="left:73px"></div>
<h3 class="abs heading widget-title" style="left:92px">Tracking</h3>
<div class="abs field" style="left:92px;top:1542px;width:296px">Reference or Bill of Lading</div>
<div class="abs field" style="left:92px;top:1591px;width:296px">Container</div>
<a class="abs btn-orange" style="left:92px;top:1649px;width:138px;height:39px">Track it</a>

<!-- testimonials -->
<h3 class="abs heading testimonial-title">Testimonials</h3>
<p class="abs testimonial-quote"><span class="quote-mark">&ldquo;</span>Lorem ipsum dolor sit amet, consectetur adipiscing elit, sed do eiusmod tempor incididunt ut labore et dolore magna aliqua. Ut enim ad minim veniam, quis nostrud exercitation ullamco laboris nisi ut.<span class="quote-mark">&rdquo;</span></p>
<p class="abs testimonial-name">Marcus Delaney</p>
<p class="abs testimonial-role">Lorem ipsum dolor</p>
<div class="abs dots"><i></i><i></i><i></i></div>

<!-- quote -->
<div class="abs widget" style="left:793px"></div>
<h3 class="abs heading widget-title" style="left:812px">Get a quote</h3>
<div class="abs field" style="left:812px;top:1542px;width:189px">City</div>
<div class="abs field select" style="left:1010px;top:1542px;width:98px">State</div>
<div class="abs field" style="left:812px;top:1591px;width:189px">City</div>
<div class="abs field select" style="left:1010px;top:1591px;width:98px">State</div>
<a class="abs btn-orange" style="left:812px;top:1649px;width:138px;height:39px">Submit</a>

<!-- promos -->
<article class="abs promo" style="left:73px">
  <div class="promo-photo" role="img" aria-label="Photo of a container handler loading a truck at a port" style="background:linear-gradient(135deg,#2b3240 0%,#4a4a46 55%,#6a5534 100%)"></div>
  <h3 class="abs promo-title">Making<br>Transportation<br>Fast and Safe</h3>
  <p class="abs promo-text">orem ipsum dolor sit amet, consectetur adipiscing elit, sed do eiusmod tempor incididunt ut labore.</p>
  <a class="abs btn-yellow promo-btn">Learn more</a>
</article>
<article class="abs promo" style="left:613px">
  <div class="promo-photo" role="img" aria-label="Photo of a truck driver standing beside his cab" style="background:linear-gradient(135deg,#2f3334 0%,#44494a 55%,#5d6360 100%)"></div>
  <h3 class="abs promo-title">Become<br>a Twin Ridge<br>Truck Driver</h3>
  <p class="abs promo-text">orem ipsum dolor sit amet, consectetur adipiscing elit, sed do eiusmod tempor incididunt ut labore.</p>
  <a class="abs btn-yellow promo-btn">Learn more</a>
</article>

<footer class="abs site-footer"></footer>
<h4 class="abs footer-title" style="left:73px">Quick Links</h4>
<ul class="abs quick-links">
  <li>Home</li><li>About</li><li>News and Events</li><li>Services</li><li>Contact</li>
</ul>
<h4 class="abs footer-title" style="left:343px">Contact Address</h4>
<div class="abs map" role="img" aria-label="Street map of the Kansas City area"></div>
<div class="abs contact-info">Kansas City, KS<br>913-555-0148<br>info@trf.example</div>
<div class="abs social footer-social"><i></i><i></i><i></i></div>
<div class="abs footer-field" style="left:757px;top:2186px;width:179px;height:38px">Name</div>
<div class="abs footer-field" style="left:945px;top:2186px;width:180px;height:38px">Email</div>
<div class="abs footer-field" style="left:757px;top:2235px;width:368px;height:65px">Message</div>
<a class="abs btn-orange" style="left:757px;top:2309px;width:211px;height:39px">Send message</a>
<div class="abs copyright"><span>Copyright © 2017 Twin Ridge Freight Inc</span>|<span>Terms</span>|<span>All Rights Reserved</span></div>

</body>
</html>
```